Local Motorsports Photography Business Card Design

Looking for a Logo and Business Card design for my father who is a local photographer based in Perth operating under the business name "KLV Photography". Specializing in Motorsports (Torque Racers/Gridcycles/Vorlen Rally) and events photography.
Would like it to look professional, while still maintaining a local/personal feel. Color\Design of the Logo and Card are open to your own interpretation, but should limit the color scheme to around 2-3 colors.
Design should be a logo one side and contact details on the rear. The website currently is very simple and a generic template and should not be used as a basis for design.
Industry/Entity Type
Business
Contact Information for Business Card
Name: Gareth Pindle
Website: www.klvphotography-example.com.au
Email: gareth@klvphotography-example.com.au
Phone: 0455 917 263
Look and feel
Each slider illustrates characteristics of the customer's brand and the style your logo design should communicate.

```html
<!DOCTYPE html>
<html lang="en">
<head>
<meta charset="utf-8">
<title>KLV Photography – Business Card</title>
<link href="https://fonts.googleapis.com/css2?family=Questrial&display=swap" rel="stylesheet">
<style>
  :root {
    --page-bg: #f3f3f4;
    --card-bg: #e8e9eb;
    --ink: #1c1c1c;
    --card-edge: #d6d7da;
  }
  * { margin: 0; padding: 0; box-sizing: border-box; }
  html, body {
    width: 1200px; height: 720px; overflow: hidden;
    background: var(--page-bg);
    font-family: "Questrial", "Century Gothic", sans-serif;
    color: var(--ink);
  }
  .canvas {
    position: relative; width: 1200px; height: 720px;
    display: flex; align-items: center; justify-content: center; gap: 60px;
  }
  .card {
    width: 500px; height: 286px;
    background: var(--card-bg);
    border: 1px solid var(--card-edge);
    display: flex; flex-direction: column; align-items: center;
  }
  .card--front { justify-content: center; }
  .brand {
    display: flex; align-items: center; gap: 14px;
  }
  .brand__mark {
    width: 16px; height: 16px; background: var(--ink);
  }
  .brand__name {
    font-size: 38px; letter-spacing: 2px; color: var(--ink);
  }
  .card--back { padding-top: 56px; }
  .camera-icon { width: 34px; height: 24px; margin-bottom: 6px; }
  .contact__name { font-size: 28px; letter-spacing: 0.5px; margin-bottom: 14px; }
  .contact__line { font-size: 15px; line-height: 21px; }
  .contact__web { font-size: 15px; margin-top: 38px; letter-spacing: 0.3px; }
</style>
</head>
<body>
  <main class="canvas">
    <section class="card card--front" aria-label="Card front">
      <div class="brand">
        <span class="brand__mark"></span>
        <span class="brand__name">KLV Photography</span>
      </div>
    </section>

    <section class="card card--back" aria-label="Card back">
      <svg class="camera-icon" viewBox="0 0 34 24" aria-hidden="true">
        <rect x="0" y="3" width="34" height="21" fill="#1c1c1c"/>
        <rect x="3" y="0" width="8" height="4" fill="#1c1c1c"/>
        <circle cx="18" cy="14" r="6" fill="none" stroke="#e8e9eb" stroke-width="2"/>
      </svg>
      <h1 class="contact__name">Gareth Pindle</h1>
      <p class="contact__line">Phone: 0455 917 263</p>
      <p class="contact__line">Email: gareth@klvphotography-example.com</p>
      <p class="contact__web">www.klvphotography-example.com.au</p>
    </section>
  </main>
</body>
</html>
```